New Business Card for Auto Repair and Performance Shop!

Need a redesign on a card that we have used for a while now. Something more update and modern, Serious but not too serious. Something confident, that shows the client that we are bespoke. Adding value.

Target Market(s)

Foreign Auto Repair and Performance

Industry/Entity Type

Automotive

Contact Information for Business Card

Utilize Logo, would like to change car silhouette to something Veltra,

Font styles to use
Sans Serif

Requirements
Must have
• business name, address, website, phone number.
MotoSerenix
4918 W. Birchwell Rd
Harlow Springs, H.S. 40917
1-555-487-3106
www.moto-serenix-example.com

Specializing in Asian, European, and Domestic Auto Repair, Performance and Fabrication.

Clear space on back to for space to write appointment time and which client advisor helped the client.
Nice to have
• Up to the designers,

```html
<!DOCTYPE html>
<html lang="en">
<head>
<meta charset="utf-8">
<title>MotoSerenix Business Card</title>
<link rel="stylesheet" href="https://fonts.googleapis.com/css2?family=Saira+Semi+Condensed:wght@600&family=PT+Sans:wght@400;700&family=Noto+Serif:wght@400&display=swap">
<style>
  :root {
    --canvas: #e9e7e3;
    --card-black: #1b1b1b;
    --paper: #ffffff;
    --ink-white: #f4f4f4;
    --accent-red: #b8232b;
    --accent-blue: #3fa6d6;
    --rule-grey: #8a8a8a;
    --text-dark: #333333;
  }
  * { box-sizing: border-box; margin: 0; padding: 0; }
  html, body { width: 1200px; height: 871px; overflow: hidden; }
  body {
    background: var(--canvas);
    display: flex;
    align-items: center;
    justify-content: center;
    gap: 60px;
  }
  .card {
    position: relative;
    width: 540px;
    height: 309px;
    box-shadow: 0 6px 18px rgba(0,0,0,0.18);
  }

  /* ---------- front ---------- */
  .card-front { background: var(--card-black); color: var(--ink-white); }
  .front-frame {
    position: absolute;
    border: 1.5px solid var(--accent-red);
  }
  .front-frame.outer { inset: 10px; }
  .front-frame.inner { inset: 18px; border-color: var(--accent-blue); }
  .front-content {
    position: absolute;
    left: 0; right: 0; top: 44px;
    text-align: center;
  }
  .business-name {
    font-family: "Saira Semi Condensed", sans-serif;
    font-weight: 600;
    font-size: 40px;
    line-height: 1;
    color: var(--ink-white);
    letter-spacing: 0.5px;
  }
  .contact-icons {
    display: flex;
    align-items: center;
    justify-content: center;
    gap: 10px;
    margin-top: 10px;
  }
  .contact-icons .rule { width: 40px; height: 1px; background: var(--ink-white); }
  .contact-icons svg { width: 13px; height: 13px; }
  .contact-lines {
    font-family: "Noto Serif", serif;
    font-size: 18px;
    line-height: 1.55;
    margin-top: 12px;
  }
  .contact-lines .web { font-size: 20px; }
  .front-mark {
    position: absolute;
    right: 40px; bottom: 40px;
    display: flex; align-items: center; gap: 6px;
    font-family: "PT Sans", sans-serif;
    font-weight: 700;
    font-size: 13px;
    letter-spacing: 1px;
    color: var(--ink-white);
  }
  .mark-square { width: 10px; height: 10px; background: var(--ink-white); }

  /* ---------- back ---------- */
  .card-back { display: flex; background: var(--card-black); }
  .appointment-panel {
    position: relative;
    width: 216px;
    background: var(--paper);
    padding: 22px 20px;
    font-family: "Noto Serif", serif;
    font-size: 11px;
    color: var(--text-dark);
  }
  .appointment-panel::before {
    content: "";
    position: absolute;
    inset: 8px;
    border: 1.5px solid var(--accent-red);
  }
  .field-label { display: flex; align-items: flex-end; gap: 4px; }
  .field-label .write-line { flex: 1; }
  .write-line { height: 1px; background: var(--rule-grey); }
  .write-stack { display: flex; flex-direction: column; gap: 20px; margin-top: 20px; }
  .field + .field { margin-top: 22px; }
  .specialty-panel {
    position: relative;
    flex: 1;
    color: var(--ink-white);
    font-family: "PT Sans", sans-serif;
    text-align: center;
  }
  .specialty-frame {
    position: absolute;
    inset: 16px;
    border: 1.5px solid var(--ink-white);
  }
  .specialty-mark {
    position: absolute;
    top: 96px; left: 0; right: 0;
    display: flex; justify-content: center; align-items: center; gap: 8px;
    font-weight: 700;
    font-size: 22px;
    letter-spacing: 1.5px;
  }
  .specialty-mark .mark-square { width: 14px; height: 14px; background: var(--accent-red); }
  .specialty-copy {
    position: absolute;
    top: 150px; left: 24px; right: 24px;
    font-size: 12.5px;
    line-height: 1.4;
  }
  .specialty-web {
    position: absolute;
    bottom: 9px; left: 0; right: 0;
    font-family: "Noto Serif", serif;
    font-size: 10.5px;
  }
  .specialty-web span { background: var(--card-black); padding: 0 8px; }
</style>
</head>
<body>

<section class="card card-front" aria-label="Business card front">
  <div class="front-frame outer"></div>
  <div class="front-frame inner"></div>
  <div class="front-content">
    <h1 class="business-name">MotoSerenix</h1>
    <div class="contact-icons">
      <span class="rule"></span>
      <svg viewBox="0 0 16 16" fill="none" stroke="#f4f4f4" stroke-width="1.3" aria-label="Location">
        <path d="M8 15s5-5.2 5-8.5A5 5 0 0 0 3 6.5C3 9.8 8 15 8 15z"/><circle cx="8" cy="6.5" r="1.8"/>
      </svg>
      <svg viewBox="0 0 16 16" fill="none" stroke="#f4f4f4" stroke-width="1.3" aria-label="Phone">
        <path d="M4 2l2.5 3-1.5 1.5a8 8 0 0 0 4.5 4.5L11 9.5l3 2.5-1.5 2C7 14 2 9 2 3.5z"/>
      </svg>
      <svg viewBox="0 0 16 16" fill="none" stroke="#f4f4f4" stroke-width="1.2" aria-label="Website">
        <circle cx="8" cy="8" r="6.3"/><ellipse cx="8" cy="8" rx="2.8" ry="6.3"/><path d="M1.7 8h12.6"/>
      </svg>
      <span class="rule"></span>
    </div>
    <p class="contact-lines">
      4918 W. Birchwell Rd, Harlow Springs, H.S. 40917<br>
      1-555-487-3106<br>
      <span class="web">www.moto-serenix-example.com</span>
    </p>
  </div>
  <div class="front-mark"><span class="mark-square"></span>MOTOSERENIX</div>
</section>

<section class="card card-back" aria-label="Business card back">
  <div class="appointment-panel">
    <div class="field">
      <div class="field-label">Appointment time - <span class="write-line"></span></div>
      <div class="write-stack">
        <span class="write-line"></span><span class="write-line"></span>
        <span class="write-line"></span><span class="write-line"></span>
      </div>
    </div>
    <div class="field">
      <div class="field-label">client advisor - <span class="write-line"></span></div>
      <div class="write-stack">
        <span class="write-line"></span><span class="write-line"></span>
      </div>
    </div>
  </div>
  <div class="specialty-panel">
    <div class="specialty-frame"></div>
    <div class="specialty-mark"><span class="mark-square"></span>MOTOSERENIX</div>
    <p class="specialty-copy">
      Specializing in<br>
      Asian, European, and Domestic Auto Repair,<br>
      Performance and Fabrication.
    </p>
    <p class="specialty-web"><span>www.moto-serenix-example.com</span></p>
  </div>
</section>

</body>
</html>
```